Velintu Yoga Centre

• Only boutique Yoga Centre which practices Yoga in traditional way.

• Only six members in one session to provide personal attention to each member.

• Many different styles of Yoga, Meditation and Vinyasana.

• Yoga and Ayurvedic Centre provides holistic approach in many ways with Ayurvedic doctors and qualified therapists with an array of all naturopathic and Ayurvedic medicine.

• Only Ayurvedic Centre with Therapeutic massage tables with made with Medicinal wood and genuine herbal oils from India and Sri Lanka

Industry/Entity Type

Boutique

```html
<!DOCTYPE html>
<html lang="en">
<head>
<meta charset="utf-8">
<title>Velintu Yoga Centre</title>
<link rel="stylesheet" href="https://fonts.googleapis.com/css2?family=Exo+2:wght@400;500&family=Marcellus&display=swap">
<style>
  :root {
    --yellow: #f7de12;
    --forest: #24362a;
    --gold: #c9a83a;
    --leaf: #9cc23c;
    --ink: #2b2b22;
    --divider: #e9cf0c;
  }
  html, body {
    margin: 0;
    padding: 0;
    width: 1200px;
    height: 1148px;
    overflow: hidden;
    background: #ffffff;
  }
  .flyer {
    position: relative;
    width: 1200px;
    height: 1148px;
    background: var(--yellow);
    font-family: "Exo 2", "Helvetica Neue", Arial, sans-serif;
    color: var(--ink);
  }
  .hero-photo {
    position: absolute;
    left: 0; top: 0;
    width: 601px; height: 572px;
    background:
      radial-gradient(ellipse 45% 55% at 52% 45%, #5a4a6e 0%, rgba(90,74,110,0) 70%),
      linear-gradient(180deg, #6f8f3a 0%, #9aa848 35%, #b8912a 70%, #d6a52a 100%);
  }
  .hero-label {
    position: absolute;
    left: 0; top: 136px;
    width: 284px; height: 114px;
    background: var(--forest);
    color: #ffffff;
    font-family: "Marcellus", Georgia, serif;
    text-align: center;
    box-sizing: border-box;
    padding-top: 14px;
  }
  .hero-label .name { font-size: 38px; line-height: 40px; letter-spacing: 1px; }
  .hero-label .line2 { font-size: 30px; line-height: 32px; letter-spacing: 2px; }
  .hero-label .line3 {
    font-size: 14px; letter-spacing: 3px; margin-top: 4px;
    border-top: 1px solid rgba(255,255,255,0.6);
    display: inline-block; padding-top: 3px;
  }
  .brand-panel {
    position: absolute;
    left: 770px; top: 0;
    width: 258px; height: 467px;
    background: var(--forest);
    text-align: center;
    color: var(--leaf);
    font-family: "Marcellus", Georgia, serif;
  }
  .brand-panel .mark {
    display: block;
    margin: 106px auto 0;
    width: 180px; height: 180px;
    border-radius: 50%;
    background: var(--leaf);
  }
  .brand-panel .brand-name {
    margin-top: 22px;
    font-size: 29px;
    line-height: 34px;
    letter-spacing: 1px;
  }
  .brand-panel .brand-sub { font-size: 15px; letter-spacing: 3px; line-height: 26px; }
  .section-rule {
    position: absolute;
    left: 601px; top: 572px;
    width: 599px; height: 1px;
    background: var(--divider);
  }
  .features {
    position: absolute;
    margin: 0;
    padding: 0 0 0 26px;
    font-size: 19.5px;
    line-height: 26px;
    list-style: disc;
  }
  .features li { margin-bottom: 26px; padding-left: 6px; }
  .features--yoga { left: 40px; top: 698px; width: 330px; }
  .features--ayurveda { left: 802px; top: 692px; width: 345px; }
  .emblem {
    position: absolute;
    left: 449px; top: 698px;
    width: 284px; height: 284px;
    border-radius: 50%;
    background: var(--forest);
  }
  .footer-rule {
    position: absolute;
    left: 4px; top: 1046px;
    width: 1196px; height: 2px;
    background: var(--ink);
  }
  .contact {
    position: absolute;
    top: 1078px;
    font-size: 18px;
    line-height: 27px;
  }
  .contact--web { left: 36px; }
  .contact--address { left: 685px; }
</style>
</head>
<body>
  <main class="flyer">
    <div class="hero-photo" role="img" aria-label="Photo of a woman meditating cross-legged on autumn leaves in a forest"></div>
    <div class="hero-label">
      <div class="name">VELINTU</div>
      <div class="line2">AYURVEDIC</div>
      <div class="line3">WELLNESS CENTRE</div>
    </div>

    <div class="brand-panel">
      <span class="mark"></span>
      <div class="brand-name">VELINTU<br>AYURVEDIC</div>
      <div class="brand-sub">WELLNESS CENTRE</div>
    </div>

    <div class="section-rule"></div>

    <ul class="features features--yoga">
      <li>Only boutique Yoga Centre which practices Yoga in traditional way.</li>
      <li>Only six members in one session to provide personal attention to each member.</li>
      <li>Many different styles of Yoga, Meditation and Vinyasana.</li>
    </ul>

    <div class="emblem" role="img" aria-label="Dark green seal ornament with a gold Om symbol"></div>

    <ul class="features features--ayurveda">
      <li>Yoga and Ayurvedic Centre provides holistic approach in many ways with Ayurvedic doctors and qualified therapists with an array of all naturopathic and Ayurvedic medicine.</li>
      <li>Only Ayurvedic Centre with Therapeutic massage tables with made with Medicinal wood and genuine herbal oils from India and Sri Lanka</li>
    </ul>

    <div class="footer-rule"></div>
    <div class="contact contact--web">Please visit<br>www.velintu.com.au | hello@velintu.com.au | call 95550142</div>
    <div class="contact contact--address">Address:<br>47 Marlow Street, Eastfield VIC 3190</div>
  </main>
</body>
</html>
```